Tildens Biscuit Barn Website

I need a website for a diner/restaurant that has been established in a farming, oil and industrial community for over 15 years. The website needs to be simple in design, but that should demonstrate the mastery of skills of the designer. Our diner/restaurant is family oriented, patriotic but very rustic
Fb Address is fb.me/TildensBarn

Pictures of the restaurant

https://www.filecrate-example.net/s/qk72hdw01/Tildens_05.jpg

Pictures of About us

https://www.filecrate-example.net/sh/zm40vrt88/AboutUsPhotos

Article about Tilden's
https://www.filecrate-example.net/s/wp31nbx57/TildensBiscuitBarn1.PDF
https://www.filecrate-example.net/s/hy65lcu29/TildensBiscuitBarn2.PDF

Reason: I was slow to update with information.

Reason: I am just getting feedback to the designs posted. I wasn't sure of the limited feedback was limiting designers from submitting designs. That and running a business with 25 employees open 12 hours a day, being here 2 hours prior and 2-3 hours after makes for long days.

I've increased the first place prize and also added funds to the second and third place prizes for your effort.

I just need the files in PSD, not HTML 5 as originally requested. We can handle getting the coding part.

Ill have the contest finalized by Monday. Thanks for your patience.

Target Market(s)

Cross section of adults from 18-35 & 35-55.

Industry/Entity Type

Industrial

Font styles to use
Other font styles liked:
• ff tisa web pro or garamond premier pro

Requirements
Must have
• Must be clean, look nice and not look like an afterthought.
Nice to have
• Please see the last two documents for information about our restaurant, which was featured in our local newspaper.

```html
<!DOCTYPE html>
<html lang="en">
<head>
<meta charset="utf-8">
<title>Tildens Biscuit Barn</title>
<link rel="stylesheet" href="https://fonts.googleapis.com/css2?family=EB+Garamond:wght@400;500&family=Kaushan+Script&family=Dancing+Script:wght@700&family=Playball&display=swap">
<style>
  :root {
    --crimson: #a5192f;
    --ink: #2a2624;
    --paper-light: #f3f2ef;
    --paper-dark: #e1dfdb;
    --plank-light: #f1f1f0;
    --plank-grey: #d9d9d8;
    --chalk-black: #0c0c0c;
    --chalk-grey: #2a2a2a;
    --chalk-white: #ececec;
    --trim-tan: #e2ac69;
    --wood-dark: #4b2e1f;
    --wood-mid: #7a5038;
    --logo-teal: #2f6077;
  }
  * { margin: 0; padding: 0; box-sizing: border-box; }
  html, body { width: 1068px; height: 1200px; overflow: hidden; background: var(--wood-dark); }
  .site { position: relative; width: 1068px; height: 1200px; font-family: "EB Garamond", Garamond, serif; color: var(--ink); }

  .site-header {
    position: absolute; left: 0; top: 0; width: 1068px; height: 232px;
    background: linear-gradient(180deg, var(--plank-light) 0%, #fbfbfb 30%, var(--plank-grey) 55%, #f6f6f6 75%, var(--plank-light) 100%);
  }
  .brand { position: absolute; left: 60px; top: 22px; width: 160px; height: 180px; }
  .brand-ring { position: absolute; left: 18px; top: 0; width: 120px; height: 120px; border: 6px solid var(--logo-teal); border-radius: 50%; }
  .brand-name {
    position: absolute; left: 0; top: 128px; width: 160px; text-align: center;
    font-size: 38px; font-weight: 500; color: var(--crimson); line-height: 1;
  }
  .welcome {
    position: absolute; left: 355px; top: 28px; width: 540px; text-align: center;
    font-family: "Kaushan Script", cursive; font-size: 118px; line-height: 1.2; color: var(--crimson);
  }

  .trim { position: absolute; left: 0; width: 1068px; height: 9px; background: var(--trim-tan); }
  .trim-top { top: 232px; }
  .trim-bottom { top: 443px; }

  .main-nav {
    position: absolute; left: 0; top: 241px; width: 1068px; height: 202px;
    background: radial-gradient(ellipse at 50% 40%, var(--chalk-grey) 0%, var(--chalk-black) 75%);
  }
  .nav-item { position: absolute; top: 22px; width: 180px; text-align: center; }
  .nav-icon { display: block; margin: 0 auto; width: 110px; height: 115px; }
  .nav-label {
    display: block; margin-top: 6px; font-family: "Playball", cursive;
    font-size: 38px; line-height: 1.1; color: var(--chalk-white);
  }
  .nav-home { left: 68px; }
  .nav-menu { left: 300px; }
  .nav-news { left: 542px; }
  .nav-founder { left: 788px; }
  .nav-founder .nav-label { font-size: 31px; margin-top: 12px; }

  .content-area {
    position: absolute; left: 0; top: 452px; width: 1068px; height: 748px;
    background: repeating-linear-gradient(180deg, var(--wood-mid) 0 52px, var(--wood-dark) 52px 57px);
  }
  .paper {
    position: absolute; left: 84px; top: 0; width: 904px; height: 712px;
    background: radial-gradient(ellipse at 50% 45%, var(--paper-light) 0%, var(--paper-dark) 100%);
  }
  .intro {
    position: absolute; left: 50px; top: 66px; width: 806px;
    font-size: 27px; line-height: 1.33; text-align: justify; text-align-last: center;
  }
  .find-us {
    position: absolute; left: 0; top: 228px; width: 904px; text-align: center;
    font-family: "Dancing Script", cursive; font-weight: 700; font-size: 76px; line-height: 1.2; color: var(--crimson);
  }
  .hours { position: absolute; top: 378px; left: 0; width: 904px; height: 50px; font-size: 36px; line-height: 1.2; }
  .hours-days { position: absolute; left: 82px; }
  .hours-dot { position: absolute; left: 430px; }
  .hours-time { position: absolute; right: 60px; }
  .contact { position: absolute; left: 0; top: 482px; width: 904px; text-align: center; font-size: 36px; line-height: 1.24; }
  .payment { position: absolute; left: 0; top: 600px; width: 904px; text-align: center; font-size: 28px; line-height: 1.27; }
</style>
</head>
<body>
<div class="site">
  <header class="site-header">
    <div class="brand">
      <div class="brand-ring"></div>
      <div class="brand-name">Tilden's</div>
    </div>
    <h1 class="welcome">Welcome</h1>
  </header>
  <div class="trim trim-top"></div>

  <nav class="main-nav">
    <a class="nav-item nav-home">
      <svg class="nav-icon" viewBox="0 0 110 115" role="img" aria-label="Chalk-drawn house icon">
        <rect x="5" y="5" width="100" height="105" rx="6" fill="#cfcfcf"/>
      </svg>
      <span class="nav-label">Home</span>
    </a>
    <a class="nav-item nav-menu">
      <svg class="nav-icon" viewBox="0 0 110 115" role="img" aria-label="Chalk-drawn crossed fork and spoon icon">
        <rect x="5" y="5" width="100" height="105" rx="6" fill="#cfcfcf"/>
      </svg>
      <span class="nav-label">Menu</span>
    </a>
    <a class="nav-item nav-news">
      <svg class="nav-icon" viewBox="0 0 110 115" role="img" aria-label="Chalk-drawn newspaper icon">
        <rect x="5" y="5" width="100" height="105" rx="6" fill="#cfcfcf"/>
      </svg>
      <span class="nav-label">News</span>
    </a>
    <a class="nav-item nav-founder">
      <svg class="nav-icon" viewBox="0 0 110 115" role="img" aria-label="Chalk portrait of the founder in a hard hat">
        <rect x="5" y="5" width="100" height="105" rx="6" fill="#bdbdbd"/>
      </svg>
      <span class="nav-label">Our founder</span>
    </a>
  </nav>
  <div class="trim trim-bottom"></div>

  <main class="content-area">
    <section class="paper">
      <p class="intro">Text about the coffee shop, its qualities, etc. Lorem ipsum dolor sit amet, consectetur adipiscing elit. Nunc vestibulum ipsum condimentum mauris porta efficitur. Morbi ut lorem sed elit interdum convallis.</p>
      <h2 class="find-us">Find Us</h2>
      <p class="hours">
        <span class="hours-days">Monday to Sunday</span>
        <span class="hours-dot">•</span>
        <span class="hours-time">5:30 AM to 2:00 PM</span>
      </p>
      <p class="contact">10480 Cedar Ridge Highway<br>555-0147</p>
      <p class="payment">NorthStar Card, Ridgeway, Summit Express,<br>Trailhead and personal checks accepted.</p>
    </section>
  </main>
</div>
</body>
</html>
```